'TOLVANTA' NEW WINE LABEL DESIGN

I am looking for an exceptional and exciting design for a wine label called 'Tolvanta' meaning 'Lookout'. The design must feature the name 'Tolvanta', and the word 'Cabernet Sauvignon' in version 1 and 'Sauvignon Blanc' in version 2. It will also need the words 'Valle Central, Chile' at the bottom of the label as a prominent piece of information as well as the vintage 2017. Please produce the work in size 80mm x 100mm. Feel free to use colour in addition to black/white and ensue that the label is easy to read on a shelf placement.
Target Market(s)
SUPERMARKETS & WINE STORES
Requirements
Must have
- EASY TO READ, USE COLOURS LIKE GREEN FOR SAUVIGNON & RED FOR CABERNET SAUVIGNON
- FULL BOTTLE SHOT MUST BE IN PROVIDED DESIGNS. ALL BOTTLE TOPS SHOULD BE QUORLAN STYLE (SCREW TOP)
- PLEASE NOTE THAT LABEL INFORMATION MUSY BE EASY TO READ I.E. VINTAGE, PLACE OF ORGIN ALTHOUGH NOT THE MAIN CONTENT MUST STILL BE CLEAR.
Nice to have
- ARTISTIC REFERENCE LINK TO NAME & ANDES BUT NOT PICTURES OF MOUNTAINS
Should not have
- PICTURES OF GRAPES
- PICTURES OF VINEYARDS
- PICTURES OF MOUNTAINS

```html
<!DOCTYPE html>
<html lang="en">
<head>
<meta charset="utf-8">
<title>Tolvanta – Cabernet Sauvignon label</title>
<link rel="stylesheet" href="https://fonts.googleapis.com/css2?family=Cinzel:wght@400;500&family=Marcellus&display=swap">
<style>
  :root {
    --backdrop: #cfc5bc;
    --label: #2a2a2b;
    --panel: #050505;
    --copper: #c47a4f;
    --ink-light: #e6e6e6;
    --rule: #9a9a9a;
    --cabernet-red: #c0161c;
  }
  * { margin: 0; padding: 0; box-sizing: border-box; }
  html, body { width: 1200px; height: 1200px; overflow: hidden; }
  body {
    background: var(--backdrop);
    font-family: "Marcellus", "Cinzel", serif;
    position: relative;
  }
  .label {
    position: absolute;
    left: 120px;
    top: 220px;
    width: 960px;
    height: 760px;
    background: var(--label);
    overflow: hidden;
    box-shadow: 0 10px 30px rgba(0,0,0,0.25);
  }
  .label__frame {
    position: absolute;
    border: 2px solid var(--copper);
  }
  .label__frame--outer { inset: 18px; }
  .label__frame--inner { inset: 28px; }
  .label__vine-panel {
    position: absolute;
    left: 560px;
    top: 0;
    width: 250px;
    height: 380px;
    background: var(--panel);
    display: flex;
    align-items: center;
    justify-content: center;
  }
  .label__vine-art {
    width: 190px;
    height: 290px;
    background: radial-gradient(ellipse at 50% 40%, #b8764d 0%, #7a4a30 55%, var(--panel) 80%);
    border-radius: 40%;
  }
  .label__monogram-panel {
    position: absolute;
    left: 460px;
    top: 625px;
    width: 270px;
    height: 135px;
    background: var(--panel);
    display: flex;
    align-items: center;
    justify-content: center;
  }
  .label__monogram-name {
    font-family: "Cinzel", serif;
    font-weight: 400;
    color: var(--copper);
    font-size: 32px;
    letter-spacing: 3px;
  }
  .label__name {
    position: absolute;
    left: 70px;
    top: 360px;
    font-family: "Cinzel", serif;
    font-weight: 400;
    font-size: 62px;
    color: var(--copper);
    letter-spacing: 1px;
  }
  .label__details {
    position: absolute;
    left: 470px;
    top: 410px;
    width: 260px;
    color: var(--ink-light);
  }
  .label__line {
    padding: 8px 0 6px;
    border-bottom: 1.5px solid var(--rule);
    font-size: 20px;
    letter-spacing: 1px;
    white-space: nowrap;
  }
  .label__vintage-year { font-family: "Cinzel", serif; font-size: 30px; font-weight: 500; margin-right: 14px; }
  .label__vintage-word { font-size: 19px; letter-spacing: 3px; }
  .label__varietal { color: var(--cabernet-red); font-size: 19px; }
</style>
</head>
<body>
  <main class="label" aria-label="Tolvanta Cabernet Sauvignon wine label">
    <div class="label__frame label__frame--outer"></div>
    <div class="label__frame label__frame--inner"></div>

    <div class="label__vine-panel">
      <div class="label__vine-art" role="img" aria-label="Copper foil illustration of a vine branch with leaves"></div>
    </div>

    <h1 class="label__name">TOLVANTA</h1>

    <div class="label__details">
      <p class="label__line"><span class="label__vintage-year">2017</span><span class="label__vintage-word">VINTAGE</span></p>
      <p class="label__line label__varietal">CABERNET SAUVIGNON</p>
      <p class="label__line">VALLE CENTRAL</p>
      <p class="label__line">CHILE</p>
    </div>

    <div class="label__monogram-panel">
      <span class="label__monogram-name">TOLVANTA</span>
    </div>
  </main>
</body>
</html>
```